KALVERIA Consultancy Business Card

We need a business card design for a new Image & Etiquette Consultancy Company.

The design should reflect the corporate colour found in the logo attached.

Info to include:

Name: Melba Tran
Title: Image Consultant
Company: KAL VERIA CONSULTANCY
Address: 27 Kelso Street, #14-09 Harbourline Tower, Singapore 058217
Contact: 9317 6284
Email: melba@kalveria.com.sg
Website: www.kalveria.com.sg

```html
<!DOCTYPE html>
<html lang="en">
<head>
<meta charset="utf-8">
<title>KALVERIA Consultancy Business Card</title>
<link rel="stylesheet" href="https://fonts.googleapis.com/css2?family=Montserrat:wght@400;600;700&display=swap">
<style>
  :root {
    --purple: #2f0f4e;
    --purple-deep: #250a40;
    --gold: #e3b23c;
    --gold-light: #f3cd62;
    --ink: #1d1426;
    --paper: #ffffff;
    --backdrop: #d9d6d2;
  }
  * { margin: 0; padding: 0; box-sizing: border-box; }
  html, body {
    width: 1200px;
    height: 655px;
    overflow: hidden;
    background: var(--backdrop);
    font-family: "Montserrat", Arial, sans-serif;
  }
  .canvas {
    position: relative;
    width: 1200px;
    height: 655px;
  }
  .card {
    position: absolute;
    width: 540px;
    height: 315px;
    overflow: hidden;
    box-shadow: 0 8px 24px rgba(0,0,0,0.25);
  }

  /* Back of card */
  .card-back {
    left: 40px;
    top: 190px;
    background: var(--purple);
  }
  .card-back .brand-name {
    position: absolute;
    left: 0;
    right: 0;
    top: 105px;
    text-align: center;
    font-size: 44px;
    font-weight: 600;
    letter-spacing: 6px;
    color: var(--gold);
  }
  .card-back .tagline-band {
    position: absolute;
    left: 130px;
    right: 60px;
    bottom: 0;
    height: 36px;
    background: linear-gradient(180deg, var(--gold-light), var(--gold));
    border-radius: 18px 18px 0 0;
    display: flex;
    align-items: center;
    justify-content: center;
    font-size: 11px;
    font-weight: 700;
    letter-spacing: 1.2px;
    color: var(--ink);
  }

  /* Front of card */
  .card-front {
    left: 620px;
    top: 170px;
    background: var(--paper);
  }
  .name-tab {
    position: absolute;
    left: 0;
    top: 22px;
    width: 230px;
    height: 26px;
    background: var(--purple);
    border-radius: 0 13px 13px 0;
    display: flex;
    align-items: center;
    padding-left: 22px;
    font-size: 12px;
    font-weight: 700;
    letter-spacing: 2.5px;
    color: var(--gold);
  }
  .job-title {
    position: absolute;
    left: 22px;
    top: 56px;
    font-size: 10px;
    font-weight: 700;
    letter-spacing: 2px;
    color: var(--ink);
  }
  .front-brand {
    position: absolute;
    right: 30px;
    top: 72px;
    font-size: 34px;
    font-weight: 600;
    letter-spacing: 5px;
    color: var(--purple);
  }
  .company-bar {
    position: absolute;
    right: 0;
    top: 150px;
    width: 280px;
    height: 26px;
    background: var(--purple);
    border-radius: 13px 0 0 13px;
    display: flex;
    align-items: center;
    justify-content: center;
    font-size: 11.5px;
    font-weight: 700;
    letter-spacing: 2px;
    color: var(--gold);
  }
  .contact-list {
    position: absolute;
    right: 22px;
    top: 186px;
    list-style: none;
    text-align: right;
  }
  .contact-item {
    display: flex;
    align-items: center;
    justify-content: flex-end;
    gap: 10px;
    margin-bottom: 9px;
    font-size: 10px;
    font-weight: 600;
    letter-spacing: 1.6px;
    line-height: 1.45;
    color: var(--ink);
  }
  .contact-icon {
    width: 16px;
    height: 16px;
    flex: none;
  }
  .web-band {
    position: absolute;
    left: 0;
    bottom: 0;
    width: 310px;
    height: 38px;
    background: var(--purple);
    border-radius: 0 19px 0 0;
    display: flex;
    align-items: center;
    padding-left: 60px;
    font-size: 11.5px;
    font-weight: 700;
    letter-spacing: 2px;
    color: var(--gold);
  }
</style>
</head>
<body>
<main class="canvas">

  <section class="card card-back" aria-label="Business card back">
    <div class="brand-name">KALVERIA</div>
    <div class="tagline-band">Image &amp; Etiquette Consultancy Company</div>
  </section>

  <section class="card card-front" aria-label="Business card front">
    <div class="name-tab">MELBA TRAN</div>
    <div class="job-title">IMAGE CONSULTANT</div>

    <div class="front-brand">KALVERIA</div>

    <div class="company-bar">KAL VERIA CONSULTANCY</div>

    <ul class="contact-list">
      <li class="contact-item">
        <span>27 KELSO STREET, #14-09, HARBOURLINE TOWER<br>SINGAPORE 058217</span>
        <svg class="contact-icon" viewBox="0 0 16 16" aria-hidden="true">
          <rect width="16" height="16" rx="2" fill="var(--purple)"/>
          <path d="M8 3.2a3 3 0 0 0-3 3c0 2.3 3 6 3 6s3-3.7 3-6a3 3 0 0 0-3-3z" fill="#fff"/>
          <circle cx="8" cy="6.2" r="1.1" fill="var(--purple)"/>
        </svg>
      </li>
      <li class="contact-item">
        <span>9317 6284</span>
        <svg class="contact-icon" viewBox="0 0 16 16" aria-hidden="true">
          <rect width="16" height="16" rx="2" fill="var(--purple)"/>
          <rect x="5" y="2.8" width="6" height="10.4" rx="1" fill="none" stroke="#fff" stroke-width="1.2"/>
          <circle cx="8" cy="11.4" r="0.7" fill="#fff"/>
        </svg>
      </li>
      <li class="contact-item">
        <span>melba@kalveria.com.sg</span>
        <svg class="contact-icon" viewBox="0 0 16 16" aria-hidden="true">
          <rect width="16" height="16" rx="2" fill="var(--purple)"/>
          <rect x="3" y="4.5" width="10" height="7" fill="none" stroke="#fff" stroke-width="1.1"/>
          <path d="M3 4.5l5 4 5-4" fill="none" stroke="#fff" stroke-width="1.1"/>
        </svg>
      </li>
    </ul>

    <div class="web-band">www.kalveria.com.sg</div>
  </section>

</main>
</body>
</html>
```